Business Card & Word Docs from existing Logo

We need a business card with typical information plus layout to include electrical contractors license number, VONEL license and KMP license. We would like a word document layout for a proposal document, opening page with logo and design basic information; proposal to and proposal from and project name and number. Small basic single page letter for general documents. Email signature with logo.

We are an electrical, refrigeration and automation contractor. We work with reducing energy consumption for our customers and complex process solutions in electrical, refrigeration and automation.

Reason: Final changes/ revisions to designs.

Target Market(s)

Industrial and commercial businesses that require more than your average contractor.

Industry/Entity Type

Electrical

Requirements
Must have
• Propsal document must have a full opening page.

```html
<!DOCTYPE html>
<html lang="en">
<head>
<meta charset="utf-8">
<title>FrostVolt Contracting – Business Card</title>
<link rel="stylesheet" href="https://fonts.googleapis.com/css2?family=Open+Sans:wght@300;400;600&display=swap">
<style>
  :root {
    --page: #ffffff;
    --card-front: #e3efe6;
    --card-back: #ffffff;
    --brand-blue: #2189b8;
    --brand-green: #2f9e47;
    --band-green: #2a9a3c;
    --text-blue: #2a7fb8;
    --shadow: rgba(0, 0, 0, 0.28);
  }
  * { box-sizing: border-box; margin: 0; padding: 0; }
  html, body {
    width: 1200px; height: 900px; overflow: hidden;
    background: var(--page);
    font-family: "Open Sans", Arial, sans-serif;
  }
  .canvas { position: relative; width: 1200px; height: 900px; }
  .card {
    position: absolute; left: 304px; width: 584px; overflow: hidden;
    box-shadow: 4px 6px 10px var(--shadow);
  }
  .card--front { top: 44px; height: 352px; background: var(--card-front); }
  .card--back { top: 504px; height: 348px; background: var(--card-back); }

  .brand { position: absolute; display: flex; align-items: center; }
  .brand__dot { border-radius: 50%; background: var(--brand-green); flex: none; }
  .brand__name { color: var(--brand-blue); font-weight: 600; }

  .card--front .brand { left: 40px; top: 0; height: 100%; gap: 28px; }
  .card--front .brand__dot { width: 200px; height: 200px; }
  .card--front .brand__name { font-size: 36px; line-height: 1.1; width: 220px; letter-spacing: -0.3px; }

  .card--back .brand { left: 34px; top: 14px; gap: 10px; }
  .card--back .brand__dot { width: 30px; height: 30px; }
  .card--back .brand__name { font-size: 18px; white-space: nowrap; }

  .holder { position: absolute; right: 36px; top: 88px; text-align: right; }
  .holder__name { font-size: 60px; font-weight: 300; color: var(--text-blue); line-height: 1.1; }
  .holder__role { font-size: 22px; color: var(--brand-green); margin-top: 4px; margin-right: 4px; }

  .contact {
    position: absolute; right: 36px; top: 228px;
    text-align: right; font-size: 11px; line-height: 15px; color: var(--text-blue);
  }
  .licences {
    position: absolute; left: 14px; top: 252px;
    font-size: 11px; line-height: 15px; color: var(--text-blue);
  }
  .web-band {
    position: absolute; left: 0; right: 0; bottom: 6px; height: 30px;
    background: var(--band-green);
    display: flex; align-items: center; padding-left: 16px;
  }
  .web-band__url { color: #fff; font-size: 17px; letter-spacing: 8px; }
</style>
</head>
<body>
<main class="canvas">
  <section class="card card--front" aria-label="Business card front">
    <div class="brand">
      <span class="brand__dot"></span>
      <span class="brand__name">FrostVolt Contracting</span>
    </div>
  </section>

  <section class="card card--back" aria-label="Business card back">
    <div class="brand">
      <span class="brand__dot"></span>
      <span class="brand__name">FrostVolt Contracting</span>
    </div>

    <div class="holder">
      <p class="holder__name">Daniel Hart</p>
      <p class="holder__role">Director</p>
    </div>

    <div class="contact">
      <p>PO Box 5521, Mackay, Queensland, 4740</p>
      <p>E-mail: daniel@frostvolt.com.au</p>
      <p>T: 07 5550 2184</p>
      <p>F: 07 5550 2185</p>
      <p>M: 0455 019 372</p>
    </div>

    <div class="licences">
      <p>Electrical Contractors License 48210</p>
      <p>KMP 7730915</p>
      <p>VONEL AU55820</p>
    </div>

    <div class="web-band">
      <span class="web-band__url">www.frostvolt.com.au</span>
    </div>
  </section>
</main>
</body>
</html>
```